Investment Funding, Building and Construction

I need a design logo for my new business based out of Houston, TX called Kestrel Ridge Holdings LLC., We are a company looking to help fund and invest into other small/businesses that do not want to deal with the banking system. We also remodel, renovate, and build from the ground up anything from residential, industrial warehousing, and commercial buildings. We would like the design to express our great deal of passion that we have for the work, our dedication to helping the costumer/businesses receive their expectation of work and also our professionalism and commitment to making sure we get the job done as perfect as possible. We want to build your future!

Target Market(s)

Architects, Design Companies, Home Owners and Real Estate

Industry/Entity Type

Construction Company

Contact Information for Business Card

Name: Dorian Welsby
Position: CEO/President
Company Name: Kestrel Ridge Holdings LLC.,
Website: www.kestrelridgeholds.example
Phone: 281-555-0173
Email: kestrelridgeholds@mailbox.example, crewfundline@mailbox.example

Font styles to use
Serif

Colors
f04a50
3377b5

Requirements
Must have
• Motivational, Inspiring, and Detailed oriented work but simple.
Nice to have
• I would like to see excitement and enthusiasm within the card.
Should not have
• The project can not be boring and lack of detail.

```html
<!DOCTYPE html>
<html lang="en">
<head>
<meta charset="utf-8">
<title>Kestrel Ridge Holdings – Business Card</title>
<link href="https://fonts.googleapis.com/css2?family=Source+Serif+4:wght@400;600&display=swap" rel="stylesheet">
<style>
  :root {
    --backdrop: #000000;
    --card-red: #f5221f;
    --card-orange: #f98a1e;
    --card-gold: #ffc805;
    --card-yellow: #fff22a;
    --brand-red: #f04a50;
    --brand-red-deep: #b51f28;
    --brand-blue: #3377b5;
    --ink-light: #ffffff;
  }
  html, body {
    margin: 0;
    padding: 0;
    width: 1200px;
    height: 1000px;
    overflow: hidden;
    background: var(--backdrop);
  }
  .canvas {
    position: relative;
    width: 1200px;
    height: 1000px;
    font-family: "Source Serif 4", serif;
    color: var(--ink-light);
  }
  .card-art {
    position: absolute;
    left: 0;
    top: 0;
  }
  .card-text {
    position: absolute;
    margin: 0;
    white-space: nowrap;
    line-height: 1;
  }
  .company-name {
    left: 290px;
    top: 371px;
    font-size: 21px;
    font-weight: 600;
  }
  .holder-name {
    left: 770px;
    top: 360px;
    transform: translateX(-50%);
    font-size: 34px;
    font-weight: 600;
    letter-spacing: 0.5px;
  }
  .holder-title {
    left: 770px;
    top: 397px;
    transform: translateX(-50%);
    font-size: 18px;
    font-weight: 400;
    letter-spacing: 1px;
  }
  .contact-line {
    left: 334px;
    font-size: 13px;
    font-weight: 400;
  }
  .address-first { top: 443px; }
  .address-second { top: 460px; }
  .email-first { top: 497px; }
  .email-second { top: 514px; }
  .phone { top: 559px; font-size: 14px; }
  .website { top: 612px; }
</style>
</head>
<body>
<div class="canvas">
  <svg class="card-art" width="1200" height="1000" viewBox="0 0 1200 1000" aria-hidden="true">
    <defs>
      <linearGradient id="panelLeft" x1="223" y1="316" x2="560" y2="720" gradientUnits="userSpaceOnUse">
        <stop offset="0" stop-color="var(--card-red)"/>
        <stop offset="0.45" stop-color="var(--card-orange)"/>
        <stop offset="0.8" stop-color="var(--card-gold)"/>
        <stop offset="1" stop-color="var(--card-yellow)"/>
      </linearGradient>
      <linearGradient id="panelRight" x1="560" y1="316" x2="977" y2="700" gradientUnits="userSpaceOnUse">
        <stop offset="0" stop-color="var(--card-red)"/>
        <stop offset="0.4" stop-color="var(--card-orange)"/>
        <stop offset="0.8" stop-color="var(--card-gold)"/>
        <stop offset="1" stop-color="var(--card-yellow)"/>
      </linearGradient>
      <linearGradient id="foldShadow" x1="617" y1="493" x2="650" y2="481" gradientUnits="userSpaceOnUse">
        <stop offset="0" stop-color="#7a1200" stop-opacity="0.65"/>
        <stop offset="1" stop-color="#7a1200" stop-opacity="0"/>
      </linearGradient>
      <linearGradient id="iconFill" x1="0" y1="0" x2="0" y2="1">
        <stop offset="0" stop-color="var(--brand-red)"/>
        <stop offset="1" stop-color="var(--brand-red-deep)"/>
      </linearGradient>
      <clipPath id="cardShape">
        <rect x="223" y="316" width="754" height="354" rx="22"/>
      </clipPath>
    </defs>

    <g class="card" clip-path="url(#cardShape)">
      <rect class="panel-left" x="223" y="316" width="754" height="354" fill="url(#panelLeft)"/>
      <polygon class="panel-right" points="552,316 977,316 977,670 682,670" fill="url(#panelRight)"/>
      <polygon class="fold-shadow" points="552,316 590,316 720,670 682,670" fill="url(#foldShadow)"/>
    </g>

    <circle class="brand-dot" cx="273" cy="381" r="10" fill="var(--brand-blue)"/>

    <g class="contact-icons" fill="var(--ink-light)">
      <g class="icon-address">
        <ellipse cx="281" cy="458" rx="22" ry="17" fill="url(#iconFill)"/>
        <path d="M281 448c-4.2 0-7 3-7 6.8 0 4.8 7 12.2 7 12.2s7-7.4 7-12.2c0-3.8-2.8-6.8-7-6.8zm0 9.3a2.6 2.6 0 1 1 0-5.2 2.6 2.6 0 0 1 0 5.2z"/>
      </g>
      <g class="icon-email">
        <ellipse cx="281" cy="512" rx="22" ry="17" fill="url(#iconFill)"/>
        <rect x="269" y="504" width="24" height="16" fill="none" stroke="var(--ink-light)" stroke-width="2"/>
        <path d="M269 504l12 9 12-9M269 520l9-8M293 520l-9-8" fill="none" stroke="var(--ink-light)" stroke-width="1.8"/>
      </g>
      <g class="icon-phone">
        <ellipse cx="281" cy="565" rx="22" ry="17" fill="url(#iconFill)"/>
        <path d="M272 555c1.5-1.3 3-1.5 3.8-.4l2.2 3.2c.6 1 .3 2-.8 2.8l-1 .7c1 2.4 3 4.6 5.5 5.8l.8-1c.8-1 1.8-1.2 2.8-.5l3.1 2.3c1 .8.8 2.3-.5 3.7-1.6 1.6-4.3 1.4-7.3-.4-3.5-2.1-6.8-5.7-8.6-9.4-1.3-2.8-1.5-5.3 0-6.8z"/>
      </g>
      <g class="icon-web">
        <ellipse cx="281" cy="618" rx="22" ry="17" fill="url(#iconFill)"/>
        <g fill="none" stroke="var(--ink-light)" stroke-width="1.7">
          <circle cx="281" cy="618" r="10"/>
          <ellipse cx="281" cy="618" rx="4.5" ry="10"/>
          <path d="M271 618h20M273 613h16M273 623h16M281 608v20"/>
        </g>
      </g>
    </g>
  </svg>

  <p class="card-text company-name">Kestrel Ridge Holdings LLC.,</p>
  <p class="card-text holder-name">DORIAN WELSBY</p>
  <p class="card-text holder-title">CEO / PRESIDENT</p>
  <p class="card-text contact-line address-first">4820 Falcon Crest Drive, Suite 210</p>
  <p class="card-text contact-line address-second">Houston, TX 77057</p>
  <p class="card-text contact-line email-first">kestrelridgeholds@mailbox.example</p>
  <p class="card-text contact-line email-second">crewfundline@mailbox.example</p>
  <p class="card-text contact-line phone">281-555-0173</p>
  <p class="card-text contact-line website">www.kestrelridgeholds.example</p>
</div>
</body>
</html>
```